Antibacterial Hand Wash Squeeze Tube Label

We're looking for a contemporary label design for a new Antibacterial Hand Wash for an 8oz squeeze tube. The new consumer brand will be sold to consumers in major US retail stores & online. The moisturizing hand wash contains Aloe Vera, vitamin E, and other natural ingredients so the design should include the color green. Real photos are very effective on packaging, so a picture of Aloe Vera or possibly two hands washing would help draw consumers' attention to the tube on the retail shelf. The front label may wrap around the sides. Rear must be left mostly blank
Target Market(s)
US Consumers - retail stores & online
Industry/Entity Type
Consumer

```html
<!DOCTYPE html>
<html lang="en">
<head>
<meta charset="utf-8">
<title>Antibacterial Hand Wash – Tube Label</title>
<link rel="stylesheet" href="https://fonts.googleapis.com/css2?family=Cinzel:wght@400;500&family=Oswald:wght@500&display=swap">
<style>
  :root {
    --green-deep: #1f6b34;
    --green-mid: #3f9a3c;
    --green-bright: #6cc04a;
    --green-pale: #a9d98c;
    --label-white: #f4f5f4;
    --label-grey: #e2e4e2;
    --ink-white: #ffffff;
  }
  * { margin: 0; padding: 0; box-sizing: border-box; }
  html, body { width: 960px; height: 1200px; overflow: hidden; background: var(--label-white); }
  .label {
    position: relative;
    width: 960px;
    height: 1200px;
    overflow: hidden;
    background: linear-gradient(90deg, var(--label-grey) 0%, var(--label-white) 25%, var(--ink-white) 50%, var(--label-white) 75%, var(--label-grey) 100%);
  }
  .label__top {
    position: absolute;
    left: 0; top: 0;
    width: 960px; height: 640px;
    border-radius: 0 0 50% 50% / 0 0 22% 22%;
    background:
      radial-gradient(ellipse at 50% 20%, var(--green-mid) 0%, transparent 60%),
      linear-gradient(180deg, var(--green-bright) 0%, var(--green-mid) 55%, var(--green-bright) 100%);
  }
  .label__title {
    position: absolute;
    left: 0; top: 110px;
    width: 960px;
    text-align: center;
    color: var(--ink-white);
    font-family: "Cinzel", serif;
    font-weight: 400;
    line-height: 1;
  }
  .label__kicker { display: block; font-size: 48px; letter-spacing: 2px; margin-bottom: 18px; }
  .label__name { display: block; font-size: 140px; letter-spacing: 2px; line-height: 0.95; }
  .label__hands-art {
    position: absolute;
    left: 340px; top: 480px;
    width: 280px; height: 230px;
    border-radius: 50%;
    background: radial-gradient(circle, var(--ink-white) 0%, var(--green-pale) 55%, transparent 75%);
  }
  .label__aloe-art {
    position: absolute;
    left: 220px; top: 730px;
    width: 520px; height: 260px;
    border-radius: 50% 50% 45% 45% / 70% 70% 30% 30%;
    background: radial-gradient(ellipse at 50% 80%, var(--green-deep) 0%, var(--green-mid) 45%, var(--green-pale) 70%, transparent 78%);
  }
  .label__band {
    position: absolute;
    left: 0; top: 1005px;
    width: 960px; height: 120px;
    background: var(--green-deep);
    display: flex;
    flex-direction: column;
    align-items: center;
    justify-content: center;
    color: var(--ink-white);
    font-family: "Cinzel", serif;
    font-size: 42px;
    letter-spacing: 3px;
    line-height: 1.15;
  }
  .label__net {
    position: absolute;
    left: 0; top: 1138px;
    width: 960px;
    text-align: center;
    font-family: "Oswald", sans-serif;
    font-weight: 500;
    font-size: 38px;
    line-height: 1.2;
    color: var(--green-deep);
  }
</style>
</head>
<body>
  <main class="label">
    <div class="label__top"></div>
    <h1 class="label__title">
      <span class="label__kicker">ANTIBACTERIAL</span>
      <span class="label__name">HAND<br>WASH</span>
    </h1>
    <div class="label__hands-art" role="img" aria-label="Illustration of two hands washing with soap bubbles"></div>
    <div class="label__aloe-art" role="img" aria-label="Illustration of an aloe vera plant with its reflection"></div>
    <div class="label__band">
      <span>ALOE VERA</span>
      <span>VITAMIN E</span>
    </div>
    <p class="label__net">80oz</p>
  </main>
</body>
</html>
```